New Optometry Practice needs a Business Card

Need a business card for an Optometry practice called 'Marlow Family Eyecare'. I would like to use designs that are friendly, fun and professional. Looking to incorporate glasses (see uploaded image). Not interested in design with an 'eye' in logo. Like green, blue, white as color choices..but open to your ideas. Back of card will be an appointment card as well as provide address, phone and email information.

Industry/Entity Type

Business

Contact Information for Business Card

Marlow Family Eyecare
Dr. Celeste Varga, Optometrist (or O.D.)
4170 S Brackenridge Rd Wenatchee, WA 98802
CMarlowfamilyeyecare.example

Colors
acd036
33b8a4
f68d4e
cfeae6
fee18a
cadf82

Requirements
Must have
• Appointment card on back with date/time of return for next exam

```html
<!DOCTYPE html>
<html lang="en">
<head>
<meta charset="utf-8">
<title>Marlow Family Eyecare – Business Card</title>
<link href="https://fonts.googleapis.com/css2?family=Source+Sans+3:ital,wght@0,400;0,600;1,400&display=swap" rel="stylesheet">
<style>
  :root {
    --backdrop: #3b3b3b;
    --card: #ffffff;
    --navy: #1e3476;
    --green: #4aa91c;
    --text-grey: #5a5a5a;
    --rule-grey: #6d6d6d;
  }
  * { box-sizing: border-box; margin: 0; padding: 0; }
  html, body {
    width: 1105px;
    height: 1200px;
    overflow: hidden;
    background: var(--backdrop);
    font-family: "Source Sans 3", "Myriad Pro", Arial, sans-serif;
  }
  .canvas { position: relative; width: 1105px; height: 1200px; }

  .card {
    position: absolute;
    left: 196px;
    width: 720px;
    height: 412px;
    background: var(--card);
    overflow: hidden;
  }
  .card--front { top: 146px; }
  .card--back { top: 600px; }

  /* Front */
  .brand-name {
    position: absolute;
    left: 86px;
    top: 168px;
    width: 290px;
    text-align: center;
    font-size: 29px;
    font-weight: 600;
    color: var(--navy);
    letter-spacing: -0.2px;
  }
  .contact { position: absolute; left: 397px; top: 122px; }
  .contact__name { font-size: 26px; font-weight: 600; color: var(--navy); line-height: 1.1; }
  .contact__title { font-size: 18px; font-weight: 600; color: var(--green); margin-top: 3px; }
  .contact__address,
  .contact__web { font-size: 19px; color: var(--text-grey); line-height: 25px; }
  .contact__address { margin-top: 14px; }
  .contact__web { margin-top: 4px; }

  .stripe-green {
    position: absolute; left: 0; right: 0; top: 379px; height: 3px;
    background: var(--green);
  }
  .stripe-navy {
    position: absolute; left: 0; right: 0; top: 384px; height: 28px;
    background: var(--navy);
  }

  /* Back */
  .appt__title {
    position: absolute; left: 0; right: 0; top: 34px;
    text-align: center;
    font-size: 31px; font-weight: 600; color: var(--navy);
  }
  .appt__rows { position: absolute; left: 46px; top: 108px; }
  .appt__row {
    display: flex; align-items: flex-end;
    height: 25px; margin-bottom: 40px;
    font-size: 19px; color: var(--text-grey);
  }
  .appt__row:nth-child(2) { margin-bottom: 38px; }
  .appt__row:nth-child(3) { margin-bottom: 40px; }
  .appt__label { width: 60px; }
  .appt__line { height: 1px; background: var(--rule-grey); margin-bottom: 5px; }
  .appt__line--date { width: 255px; margin-right: 18px; }
  .appt__label--time { width: 60px; }
  .appt__line--time { width: 136px; margin-right: 11px; }
  .appt__notice {
    position: absolute; left: 0; right: 0; top: 362px;
    text-align: center;
    font-size: 17px; font-style: italic; color: var(--text-grey);
  }
</style>
</head>
<body>
<main class="canvas">

  <section class="card card--front" aria-label="Business card front">
    <div class="brand-name">Marlow Family Eyecare</div>
    <div class="contact">
      <div class="contact__name">Dr. Celeste Varga</div>
      <div class="contact__title">Optometrist</div>
      <div class="contact__address">4170 S Brackenridge Rd<br>Wenatchee, WA 98802</div>
      <div class="contact__web">CMarlowfamilyeyecare.example</div>
    </div>
    <div class="stripe-green"></div>
    <div class="stripe-navy"></div>
  </section>

  <section class="card card--back" aria-label="Appointment card back">
    <h1 class="appt__title">Marlow Family Eyecare</h1>
    <div class="appt__rows">
      <div class="appt__row"><span class="appt__label">Date</span><span class="appt__line appt__line--date"></span><span class="appt__label appt__label--time">Time</span><span class="appt__line appt__line--time"></span><span>am/pm</span></div>
      <div class="appt__row"><span class="appt__label">Date</span><span class="appt__line appt__line--date"></span><span class="appt__label appt__label--time">Time</span><span class="appt__line appt__line--time"></span><span>am/pm</span></div>
      <div class="appt__row"><span class="appt__label">Date</span><span class="appt__line appt__line--date"></span><span class="appt__label appt__label--time">Time</span><span class="appt__line appt__line--time"></span><span>am/pm</span></div>
      <div class="appt__row"><span class="appt__label">Date</span><span class="appt__line appt__line--date"></span><span class="appt__label appt__label--time">Time</span><span class="appt__line appt__line--time"></span><span>am/pm</span></div>
    </div>
    <p class="appt__notice">Please give 24 hours notice cancelling your appointment or a fee may be charged</p>
  </section>

</main>
</body>
</html>
```